Email Sig, Letterhead, Business Card Design

Need a stationary package including email signature, letterhead/envelope, and business card design incorporating our new logo.

```html
<!DOCTYPE html>
<html lang="en">
<head>
<meta charset="utf-8">
<title>Corvane Engineering Stationery</title>
<link href="https://fonts.googleapis.com/css2?family=Roboto:wght@400;500;700&display=swap" rel="stylesheet">
<style>
:root{
  --blue:#2a5f9a;
  --blue-dark:#214d80;
  --orange:#e4572e;
  --ink:#4a4a4a;
  --paper:#ffffff;
  --bg-top:#eef0f3;
  --bg-mid:#e4e5e7;
  --bg-low:#dadbdd;
}
*{margin:0;padding:0;box-sizing:border-box}
html,body{width:1200px;height:2410px;overflow:hidden}
body{position:relative;font-family:'Roboto',sans-serif;color:var(--ink)}
.band{position:absolute;left:0;width:1200px;overflow:hidden}
.band--top{top:0;height:800px;background:var(--bg-top)}
.band--mid{top:800px;height:792px;background:var(--bg-mid)}
.band--low{top:1592px;height:818px;background:var(--bg-low)}
.sheet{position:absolute;background:var(--paper);box-shadow:0 2px 10px rgba(0,0,0,.12);overflow:hidden}
.brand{display:flex;align-items:center;gap:6px;color:var(--orange);font-weight:700;letter-spacing:.02em;white-space:nowrap}
.brand__dot{border-radius:50%;background:var(--blue);flex:none}
.brand-sub{color:var(--blue);font-size:5px;letter-spacing:.06em;text-transform:uppercase;white-space:nowrap}
.contact-line{display:flex;align-items:center;gap:4px}
.contact-line svg{flex:none}

/* Letterhead */
.letterhead{left:370px;top:60px;width:480px;height:680px}
.letterhead .brand{position:absolute;left:48px;top:66px;font-size:12px}
.letterhead .brand__dot{width:16px;height:16px}
.letterhead .brand-sub{position:absolute;left:48px;top:88px}
.letterhead__contact{position:absolute;left:316px;top:56px;font-size:8px;line-height:1.4;color:#555}
.letterhead__body{position:absolute;left:50px;top:176px;width:376px;font-size:7.6px;line-height:1.6;color:#666}
.letterhead__body p{margin-bottom:10px;text-align:justify}
.letterhead__foot{position:absolute;left:0;bottom:0;width:100%;height:16px;background:var(--blue);color:#fff;font-size:7.5px;text-align:center;line-height:16px;letter-spacing:.05em}

/* Small cards */
.card-sm{width:194px;height:120px}
.card-sm--front{left:106px;top:374px}
.card-sm--back{left:106px;top:546px;background:var(--blue)}
.card-sm--front .brand{position:absolute;left:8px;top:56px;font-size:5.5px;gap:4px}
.card-sm--front .brand__dot{width:9px;height:9px}
.card-sm__rule{position:absolute;left:98px;top:26px;width:1px;height:64px;background:#bbb}
.card-sm__info{position:absolute;left:105px;top:26px;font-size:5px;line-height:1.45;color:#555}
.name-sm{color:var(--blue);font-weight:700;font-size:6px}
.role-sm{color:var(--orange);font-size:5px}
.card-sm__strip{position:absolute;left:0;bottom:0;width:100%;height:5px;background:var(--blue)}
.card-sm__pattern{position:absolute;inset:0;background:linear-gradient(135deg,#2f68a8,#214d80)}
.card-sm--back .brand{position:absolute;right:14px;bottom:26px;font-size:7px;color:#fff}

/* Envelopes */
.envelope{width:640px;height:300px}
.envelope--back{left:470px;top:70px}
.envelope--front{left:110px;top:400px}
.envelope--front .brand{position:absolute;left:40px;top:36px;font-size:16px}
.envelope--front .brand__dot{width:22px;height:22px}
.envelope__address{position:absolute;left:40px;top:70px;font-size:11px;line-height:1.5;color:#555}
.envelope__strip{position:absolute;left:0;bottom:0;width:100%;height:28px;background:var(--blue);color:#fff;font-size:11px;line-height:28px;padding-left:40px;letter-spacing:.05em}
.envelope__flap{position:absolute;left:0;top:0;width:100%;height:100px;background:var(--blue);border-radius:0 0 18px 18px}
.envelope__flap .brand{position:absolute;left:50%;top:50%;transform:translate(-50%,-50%);color:#fff;font-size:13px}

/* Large cards */
.card-lg{width:560px;height:320px}
.card-lg--front{left:80px;top:80px}
.card-lg--back{left:560px;top:430px;background:var(--blue)}
.card-lg--front .brand{position:absolute;left:30px;top:148px;font-size:15px}
.card-lg--front .brand__dot{width:26px;height:26px}
.card-lg--front .brand-sub{position:absolute;left:30px;top:180px;font-size:6.5px;line-height:1.6}
.card-lg__rule{position:absolute;left:276px;top:60px;width:1px;height:190px;background:#999}
.card-lg__info{position:absolute;left:296px;top:60px;font-size:13px;line-height:1.55;color:#444}
.name-lg{color:var(--blue);font-weight:700;font-size:17px;letter-spacing:.02em}
.role-lg{color:var(--orange);font-weight:500;font-size:14px;margin-bottom:6px}
.card-lg__strip{position:absolute;left:0;bottom:0;width:100%;height:9px;background:var(--blue)}
.card-lg__pattern{position:absolute;inset:0;background:linear-gradient(135deg,#2f68a8,#214d80)}
.card-lg--back .brand{position:absolute;right:40px;bottom:74px;color:#fff;font-size:19px}
.card-lg--back .brand-sub{position:absolute;right:40px;bottom:46px;color:#fff;font-size:7px;text-align:right;line-height:1.6}
</style>
</head>
<body>

<section class="band band--top">
  <article class="sheet letterhead">
    <div class="brand"><span class="brand__dot"></span>CORVANE ENGINEERING</div>
    <div class="brand-sub">1420 Alder Ridge Lane, Kingwood, Texas 77000</div>
    <div class="letterhead__contact">
      <div>Suite 18/42 Elmore St</div>
      <div>Brunswick, Victoria Australia</div>
      <div class="contact-line"><svg width="7" height="7" viewBox="0 0 10 10"><path d="M2 1l2 2-1 1.5c.6 1.2 1.3 1.9 2.5 2.5L7 6l2 2-1.5 1.5C4 9 1 6 .5 2.5z" fill="#e4572e"/></svg>+61 3 5550 1274</div>
      <div class="contact-line"><svg width="7" height="7" viewBox="0 0 10 10"><rect x="1" y="3" width="8" height="5" fill="#e4572e"/><rect x="3" y="1" width="4" height="2" fill="#e4572e"/></svg>+61 3 5550 1290</div>
      <div class="contact-line"><svg width="7" height="7" viewBox="0 0 10 10"><rect x="0.5" y="2" width="9" height="6" fill="#e4572e"/><path d="M.5 2l4.5 3.5L9.5 2" stroke="#fff" fill="none"/></svg>info@corvaneeng.com</div>
    </div>
    <div class="letterhead__body">
      <p>Dear customer,</p>
      <p>Lorem ipsum dolor sit amet, consectetur adipisicing elit, sed do eiusmod tempor incididunt ut labore et dolore magna aliqua. Ut enim ad minim veniam, quis nostrud exercitation ullamco laboris nisi ut aliquip ex ea commodo consequat. Duis aute irure dolor in reprehenderit in voluptate velit esse cillum dolore eu fugiat nulla pariatur. Excepteur sint occaecat cupidatat non proident, sunt in culpa qui officia deserunt mollit anim id est laborum.</p>
      <p>Lorem ipsum dolor sit amet, consectetur adipisicing elit, sed do eiusmod tempor incididunt ut labore et dolore magna aliqua. Ut enim ad minim veniam, quis nostrud exercitation ullamco laboris nisi ut aliquip ex ea commodo consequat. Duis aute irure dolor in reprehenderit in voluptate velit esse cillum dolore eu fugiat nulla pariatur. Excepteur sint occaecat cupidatat non proident, sunt in culpa qui officia deserunt mollit anim id est laborum.</p>
      <p>Lorem ipsum dolor sit amet, consectetur adipisicing elit, sed do eiusmod tempor incididunt ut labore et dolore magna aliqua. Ut enim ad minim veniam, quis nostrud exercitation ullamco laboris nisi ut aliquip ex ea commodo consequat. Duis aute irure dolor in reprehenderit in voluptate velit esse cillum dolore eu fugiat nulla pariatur. Excepteur sint occaecat cupidatat non proident, sunt in culpa qui officia deserunt mollit anim id est laborum.</p>
      <p>Lorem ipsum dolor sit amet, consectetur adipisicing elit, sed do eiusmod tempor incididunt ut labore et dolore magna aliqua. Ut enim ad minim veniam, quis nostrud exercitation ullamco laboris nisi ut aliquip ex ea commodo consequat. Duis aute irure dolor in reprehenderit.</p>
      <p>Yours Sincerely,</p>
    </div>
    <div class="letterhead__foot">www.corvaneeng.com</div>
  </article>

  <article class="sheet card-sm card-sm--front">
    <div class="brand"><span class="brand__dot"></span>CORVANE ENGINEERING</div>
    <div class="card-sm__rule"></div>
    <div class="card-sm__info">
      <div class="name-sm">HARLOW BENNETT</div>
      <div class="role-sm">Managing Director</div>
      <div>Suite 18/42 Elmore St</div>
      <div>Brunswick, Victoria</div>
      <div>Australia</div>
      <div>+61 3 5550 1274</div>
      <div>info@corvaneeng.com</div>
      <div>www.corvaneeng.com</div>
    </div>
    <div class="card-sm__strip"></div>
  </article>

  <article class="sheet card-sm card-sm--back">
    <div class="card-sm__pattern" role="img" aria-label="Repeating embossed brand pattern on blue"></div>
    <div class="brand">CORVANE ENGINEERING</div>
  </article>
</section>

<section class="band band--mid">
  <article class="sheet envelope envelope--back">
    <div class="envelope__flap"><div class="brand">CORVANE ENGINEERING</div></div>
  </article>
  <article class="sheet envelope envelope--front">
    <div class="brand"><span class="brand__dot"></span>CORVANE ENGINEERING</div>
    <div class="envelope__address">Suite 18/42 Elmore St<br>Brunswick, Victoria Australia</div>
    <div class="envelope__strip">www.corvaneeng.com</div>
  </article>
</section>

<section class="band band--low">
  <article class="sheet card-lg card-lg--front">
    <div class="brand"><span class="brand__dot"></span>CORVANE ENGINEERING</div>
    <div class="brand-sub">1420 Alder Ridge Lane, Kingwood, Texas 77000<br>Firm Registration F-4410</div>
    <div class="card-lg__rule"></div>
    <div class="card-lg__info">
      <div class="name-lg">HARLOW BENNETT</div>
      <div class="role-lg">Managing Director</div>
      <div>Suite 18/42 Elmore St</div>
      <div>Brunswick, Victoria</div>
      <div>Australia</div>
      <div class="contact-line"><svg width="12" height="12" viewBox="0 0 10 10"><path d="M2 1l2 2-1 1.5c.6 1.2 1.3 1.9 2.5 2.5L7 6l2 2-1.5 1.5C4 9 1 6 .5 2.5z" fill="#e4572e"/></svg>+61 3 5550 1274</div>
      <div class="contact-line"><svg width="12" height="12" viewBox="0 0 10 10"><rect x="0.5" y="2" width="9" height="6" fill="#e4572e"/><path d="M.5 2l4.5 3.5L9.5 2" stroke="#fff" fill="none"/></svg>info@corvaneeng.com</div>
      <div class="contact-line"><svg width="12" height="12" viewBox="0 0 10 10"><circle cx="5" cy="5" r="4.2" fill="none" stroke="#e4572e" stroke-width="1.2"/><path d="M1 5h8M5 1c-2 2.5-2 5.5 0 8M5 1c2 2.5 2 5.5 0 8" stroke="#e4572e" fill="none" stroke-width=".8"/></svg>www.corvaneeng.com</div>
    </div>
    <div class="card-lg__strip"></div>
  </article>

  <article class="sheet card-lg card-lg--back">
    <div class="card-lg__pattern" role="img" aria-label="Repeating embossed brand pattern on blue"></div>
    <div class="brand">CORVANE ENGINEERING</div>
    <div class="brand-sub">1420 Alder Ridge Lane, Kingwood, Texas 77000<br>Firm Registration F-4410</div>
  </article>
</section>

</body>
</html>
```